Tumbleleaf Snacks Website redesign

I would like a redesign of my current website, www.tumbleleafsnacks.example. We make a pre-popped and packaged popcorn that we sell to grocers, retailers, and on-line. My current website is not appealing, and I would like to attract more customers to my online store. Our competition is Lofty Crunch, Brightbite, and Zing Zang Puff to name a few, please take a look at their sites for examples. What sets Tumbleleaf apart from competitors is our 3 ingredients, non-GMO WHITE popcorn, corn oil, kosher salt. White kernels pop up more tender and virtually hull-less with a sweet corn flavor. Tumbleleaf is all-natural, kosher, and nothing artificial.

Coding

```html
<!DOCTYPE html>
<html lang="en">
<head>
<meta charset="utf-8">
<title>Tumbleleaf Snacks – Home</title>
<link rel="stylesheet" href="https://fonts.googleapis.com/css2?family=Open+Sans:wght@400;600;700&family=Poppins:wght@400&family=Roboto:wght@400;500;700&family=Yellowtail&display=swap">
<style>
:root{
  --blue:#033b80;
  --blue-dark:#022c63;
  --yellow:#fcc30b;
  --cream:#fdf9ea;
  --ink:#1b1b1b;
  --grey-text:#555;
  --black:#000;
  --footer-bar:#141414;
  --white:#fff;
}
*{margin:0;padding:0;box-sizing:border-box}
html,body{width:1200px;height:3292px;overflow:hidden}
body{position:relative;background:var(--cream);font-family:"Open Sans",sans-serif;color:var(--ink)}
.abs{position:absolute}
.script{font-family:"Yellowtail","Brush Script MT",cursive;font-weight:400;white-space:nowrap}

/* header */
.top-line{left:0;top:0;width:1200px;height:4px;background:var(--blue)}
.header{left:0;top:4px;width:1200px;height:105px;background:var(--white)}
.brand{left:112px;top:30px;display:flex;align-items:center;gap:10px;font-family:"Open Sans",sans-serif;font-weight:700;font-size:20px;color:var(--blue);line-height:1.1}
.brand-dot{width:30px;height:30px;border-radius:50%;background:var(--yellow);flex:none}
.call-pill{left:732px;top:0;width:357px;height:48px;background:var(--blue);border-radius:0 0 26px 26px;display:flex;align-items:center;justify-content:center;gap:10px;color:var(--white);font-weight:600;font-size:15px;white-space:nowrap}
.call-pill b{color:var(--yellow);font-size:19px;font-weight:600}
.nav{top:68px;font-weight:600;font-size:14.5px;letter-spacing:.3px;color:#222;white-space:nowrap}
.nav.active{color:var(--blue)}
.nav.active::after{content:"";position:absolute;left:0;right:0;top:29px;height:3px;background:var(--blue)}

/* hero */
.hero-photo{left:0;top:109px;width:1200px;height:671px;background:linear-gradient(90deg,#7a4a2e 0%,#5b3324 30%,#2a1612 55%,#0c0706 75%,#050303 100%)}
.hero-title{left:520px;top:308px;width:610px;text-align:center;font-size:66px;color:var(--white);line-height:76px}
.hero-sub{left:570px;top:398px;width:510px;text-align:center;font-family:"Roboto",sans-serif;font-size:15px;line-height:22px;color:var(--white)}
.btn{background:var(--yellow);color:var(--white);font-weight:600;font-size:14px;border-radius:20px;display:flex;align-items:center;justify-content:center;gap:8px;letter-spacing:.2px;white-space:nowrap}
.hero-btn{left:748px;top:466px;width:150px;height:38px}
.hero-arrow{width:44px;height:44px;border-radius:50%;background:rgba(150,150,150,.75);display:flex;align-items:center;justify-content:center}
.dots{left:574px;top:623px;display:flex;gap:8px}
.dots span{width:13px;height:13px;border-radius:50%;border:2px solid var(--white)}
.dots span.on{background:var(--white)}

/* story */
.section-title{left:0;width:1200px;text-align:center;font-size:50px;line-height:60px}
.story-text{left:147px;top:883px;width:906px;font-family:"Poppins",sans-serif;font-size:15px;line-height:21.5px;color:var(--grey-text);text-align:justify;text-align-last:center}
.story-text p+p{margin-top:21px}
.read-btn{left:525px;top:1088px;width:151px;height:37px}
.popcorn-strip{left:0;top:1163px;width:1200px;height:180px;background:linear-gradient(180deg,var(--cream) 0%,#f1e2bc 22%,#e6cf98 60%,#d9bb7c 100%)}

/* products */
.products-band{left:0;top:1343px;width:1200px;height:680px;background:var(--blue)}
.product{top:1518px;width:312px;height:393px;background:var(--white)}
.product-img{left:13px;top:12px;width:286px;height:262px;border-radius:30px;background:linear-gradient(160deg,#e4e4e4,#f2f2f2 60%,#dcdcdc)}
.product-name{left:0;top:300px;width:312px;text-align:center;font-family:"Roboto",sans-serif;font-size:17px;color:var(--ink);white-space:nowrap}
.product-price{left:0;top:336px;width:312px;text-align:center;font-family:"Roboto",sans-serif;font-weight:500;font-size:26px;color:var(--blue)}
.product-bar{left:443px;top:1911px;width:312px;height:9px;background:var(--yellow)}
.zoom{left:115px;top:105px;width:56px;height:56px;border-radius:50%;background:var(--blue);display:flex;align-items:center;justify-content:center}
.slide-arrow{top:1695px;width:68px;height:68px;border-radius:50%;background:var(--yellow);display:flex;align-items:center;justify-content:center}

/* blog */
.blog-card{overflow:hidden}
.blog-img{left:0;top:0;width:100%;height:100%}
.blog-box{background:var(--white);font-family:"Roboto",sans-serif;color:var(--ink)}
.blog-date{display:flex;align-items:center;gap:7px;color:var(--blue);font-weight:500;text-decoration:underline;font-size:15px;white-space:nowrap}
.view-btn{left:556px;top:2699px;width:151px;height:38px}

/* footer */
.footer-black{left:0;top:2868px;width:1200px;height:345px;background:var(--black)}
.footer-nav{left:0;top:2966px;width:1200px;display:flex;justify-content:center;gap:18px;color:var(--white);font-weight:700;font-size:15px}
.contact{top:3021px;width:360px;text-align:center;color:var(--white)}
.contact .ico{width:54px;height:54px;border-radius:50%;background:var(--yellow);margin:0 auto 6px;display:flex;align-items:center;justify-content:center}
.contact h4{color:var(--yellow);font-weight:600;font-size:19px;line-height:26px}
.contact p{font-weight:600;font-size:19px;line-height:24px;margin-top:6px}
.copy-bar{left:0;top:3213px;width:1200px;height:79px;background:var(--footer-bar);display:flex;align-items:center;justify-content:center;color:var(--white);font-size:16px}
</style>
</head>
<body>

<!-- header -->
<div class="abs top-line"></div>
<header class="abs header"></header>
<div class="abs brand"><span class="brand-dot"></span><span>Tumbleleaf<br>Snacks</span></div>
<div class="abs call-pill">
  <svg width="14" height="18" viewBox="0 0 14 18"><rect x="2" y="1" width="10" height="16" rx="2" fill="none" stroke="#fff" stroke-width="2"/><circle cx="7" cy="14" r="1" fill="#fff"/></svg>
  <span>Call Us Anytime : <b>(555) 014-7720</b></span>
</div>
<nav>
  <div class="abs nav active" style="left:497px">HOME</div>
  <div class="abs nav" style="left:598px">ABOUT US</div>
  <div class="abs nav" style="left:728px">OUR PRODUCTS</div>
  <div class="abs nav" style="left:900px">BLOG</div>
  <div class="abs nav" style="left:997px">CONTACT US</div>
</nav>

<!-- hero -->
<div class="abs hero-photo" role="img" aria-label="Couple laughing and sharing a bucket of popcorn in a cinema"></div>
<div class="abs hero-title script">Tumbleleaf Snacks</div>
<div class="abs hero-sub">opped and distributed in California! Please ask your local store to carry Tumbleleaf- Thank you for your support!</div>
<div class="abs btn hero-btn">GET STARTED</div>
<div class="abs hero-arrow" style="left:33px;top:363px"><svg width="12" height="12" viewBox="0 0 12 12"><path d="M8 1 3 6l5 5" fill="none" stroke="#333" stroke-width="1.6"/></svg></div>
<div class="abs hero-arrow" style="left:1122px;top:363px"><svg width="12" height="12" viewBox="0 0 12 12"><path d="M4 1l5 5-5 5" fill="none" stroke="#333" stroke-width="1.6"/></svg></div>
<div class="abs dots"><span></span><span class="on"></span><span></span></div>
<svg class="abs" style="left:0;top:640px" width="1200" height="145" viewBox="0 640 1200 145">
  <path d="M0 712 C200 660 400 668 560 712 C760 770 1000 758 1200 700 L1200 785 L0 785Z" fill="var(--blue)"/>
  <path d="M0 712 C220 692 420 718 580 752 C740 786 980 788 1200 728 L1200 785 L0 785Z" fill="var(--cream)"/>
</svg>

<!-- story -->
<h2 class="abs section-title script" style="top:820px">Our Story</h2>
<div class="abs story-text">
  <p>Lorem ipsum dolor sit amet, consectetur adipiscing elit, sed do eiusmod tempor incididunt ut labore et dolore magna aliqua. Ut enim ad minim veniam, quis nostrud exercitation ullamco laboris nisi ut aliquip ex ea commodo consequat. Duis aute irure dolor in reprehenderit in voluptate velit esse cillum dolore eu fugiat nulla pariatur. Excepteur sint occaecat cupidatat non proident, sunt in culpa qui officia deserunt mollit anim id est laborum.</p>
  <p>Sed ut perspiciatis unde omnis iste natus error sit voluptatem accusantium doloremque laudantium, totam rem aperiam, eaque ipsa quae ab illo inventore veritatis et quasi architecto beatae vitae dicta sunt explicabo. Nemo enim ipsam voluptatem quia voluptas sit aspernatur aut odit aut fugit, sed quia consequuntur magni dolores eos qui ratione voluptatem sequi nesciunt.</p>
</div>
<div class="abs btn read-btn">READ MORE
  <svg width="14" height="14" viewBox="0 0 14 14"><circle cx="7" cy="7" r="7" fill="#fff"/><path d="M5.5 4l3 3-3 3" fill="none" stroke="var(--yellow)" stroke-width="1.8"/></svg>
</div>
<div class="abs popcorn-strip" role="img" aria-label="Row of freshly popped white popcorn"></div>

<!-- featured products -->
<div class="abs products-band"></div>
<h2 class="abs section-title script" style="top:1427px;color:var(--white)">Featured Products</h2>

<div class="abs product" style="left:111px">
  <div class="abs product-img" role="img" aria-label="Bag of Tumbleleaf popcorn"></div>
  <div class="abs product-name">Tumbleleaf Popcorn, case of 15</div>
  <div class="abs product-price">$65.00</div>
</div>
<div class="abs product" style="left:443px">
  <div class="abs product-img" role="img" aria-label="Bag of Tumbleleaf popcorn"></div>
  <div class="abs zoom"><svg width="18" height="18" viewBox="0 0 18 18"><circle cx="7.5" cy="7.5" r="5.5" fill="none" stroke="#fff" stroke-width="2"/><path d="M11.5 11.5 16 16M5 7.5h5M7.5 5v5" stroke="#fff" stroke-width="2"/></svg></div>
  <div class="abs product-name">Tumbleleaf Popcorn, case of 6</div>
  <div class="abs product-price">$40.00</div>
</div>
<div class="abs product-bar"></div>
<div class="abs product" style="left:776px">
  <div class="abs product-img" role="img" aria-label="Bag of Tumbleleaf popcorn"></div>
  <div class="abs product-name">Additional Shipping charges</div>
  <div class="abs product-price">$20.00</div>
</div>
<div class="abs slide-arrow" style="left:72px"><svg width="14" height="14" viewBox="0 0 14 14"><path d="M9 2 4 7l5 5" fill="none" stroke="#fff" stroke-width="2"/></svg></div>
<div class="abs slide-arrow" style="left:1060px"><svg width="14" height="14" viewBox="0 0 14 14"><path d="M5 2l5 5-5 5" fill="none" stroke="#fff" stroke-width="2"/></svg></div>

<!-- blog -->
<h2 class="abs section-title script" style="top:2095px">Latest Blog</h2>

<div class="abs blog-card" style="left:111px;top:2183px;width:470px;height:493px">
  <div class="abs blog-img" role="img" aria-label="Family enjoying popcorn and drinks at a cinema lobby" style="background:linear-gradient(160deg,#8a7466,#5e4a40 45%,#3a2e2a)"></div>
  <div class="abs blog-box" style="left:18px;top:345px;width:434px;height:130px;padding:22px 26px">
    <div style="font-weight:500;font-size:25px;line-height:30px">Lorem ipsum dolor sit amet, consectetur</div>
    <div class="blog-date" style="margin-top:12px;font-size:16px">
      <svg width="15" height="15" viewBox="0 0 15 15"><rect x="1" y="2.5" width="13" height="11.5" fill="none" stroke="var(--blue)" stroke-width="1.5"/><path d="M1 6h13M4 1v3M11 1v3" stroke="var(--blue)" stroke-width="1.5"/></svg>Nov 25,2024</div>
  </div>
</div>

<div class="abs blog-card" style="left:619px;top:2183px;width:469px;height:235px">
  <div class="abs blog-img" role="img" aria-label="Popcorn spilling from a paper bag on wood" style="background:linear-gradient(120deg,#6b4a2e,#c9a463 45%,#8a6340)"></div>
  <div class="abs blog-box" style="left:292px;top:20px;width:159px;height:197px;padding:44px 20px 0">
    <div style="font-weight:500;font-size:17px;line-height:26px">Lorem ipsum dolor sit amet, consectetur</div>
    <div class="blog-date" style="margin-top:14px">
      <svg width="14" height="14" viewBox="0 0 15 15"><rect x="1" y="2.5" width="13" height="11.5" fill="none" stroke="var(--blue)" stroke-width="1.5"/><path d="M1 6h13M4 1v3M11 1v3" stroke="var(--blue)" stroke-width="1.5"/></svg>Nov 25,2024</div>
  </div>
</div>

<div class="abs blog-card" style="left:619px;top:2442px;width:469px;height:234px">
  <div class="abs blog-img" role="img" aria-label="Couple sharing a bowl of popcorn at home" style="background:linear-gradient(120deg,#5a4638,#8d6e55 45%,#c4a98c)"></div>
  <div class="abs blog-box" style="left:292px;top:20px;width:159px;height:197px;padding:44px 20px 0">
    <div style="font-weight:500;font-size:17px;line-height:26px">Lorem ipsum dolor sit amet, consectetur</div>
    <div class="blog-date" style="margin-top:14px">
      <svg width="14" height="14" viewBox="0 0 15 15"><rect x="1" y="2.5" width="13" height="11.5" fill="none" stroke="var(--blue)" stroke-width="1.5"/><path d="M1 6h13M4 1v3M11 1v3" stroke="var(--blue)" stroke-width="1.5"/></svg>Nov 25,2024</div>
  </div>
</div>

<div class="abs btn view-btn">VIEW MORE
  <svg width="14" height="14" viewBox="0 0 14 14"><circle cx="7" cy="7" r="7" fill="#fff"/><path d="M5.5 4l3 3-3 3" fill="none" stroke="var(--yellow)" stroke-width="1.8"/></svg>
</div>

<!-- footer -->
<svg class="abs" style="left:0;top:2780px" width="1200" height="92" viewBox="0 2780 1200 92">
  <path d="M0 2850 C200 2895 380 2890 560 2840 C720 2795 900 2785 1050 2810 C1120 2822 1170 2840 1200 2855 L1200 2872 L0 2872Z" fill="var(--blue)"/>
  <path d="M0 2860 C200 2902 380 2900 560 2852 C720 2810 900 2800 1050 2825 C1120 2837 1170 2853 1200 2868 L1200 2872 L0 2872Z" fill="var(--black)"/>
</svg>
<div class="abs footer-black"></div>
<div class="abs footer-nav"><span>HOME</span><span>|</span><span>ABOUT US</span><span>|</span><span>OUR PRODUCTS</span><span>|</span><span>CONTACT US</span></div>

<div class="abs contact" style="left:82px">
  <div class="ico"><svg width="24" height="26" viewBox="0 0 24 26"><path d="M12 24s-8-8-8-14a8 8 0 0 1 16 0c0 6-8 14-8 14z" fill="none" stroke="#222" stroke-width="1.8"/><circle cx="12" cy="10" r="3" fill="none" stroke="#222" stroke-width="1.8"/></svg></div>
  <h4>Address :</h4>
  <p>123,Lorem ipsum dolor sit<br>amet, consec</p>
</div>
<div class="abs contact" style="left:408px">
  <div class="ico"><svg width="24" height="24" viewBox="0 0 24 24"><path d="M5 3h4l2 5-3 2a12 12 0 0 0 6 6l2-3 5 2v4a2 2 0 0 1-2 2A18 18 0 0 1 3 5a2 2 0 0 1 2-2z" fill="none" stroke="#222" stroke-width="1.6"/></svg></div>
  <h4>Phone :</h4>
  <p>(555) 014-7720</p>
</div>
<div class="abs contact" style="left:739px">
  <div class="ico"><svg width="26" height="20" viewBox="0 0 26 20"><rect x="1" y="1" width="24" height="18" fill="none" stroke="#222" stroke-width="1.8"/><path d="M1 1l12 10L25 1" fill="none" stroke="#222" stroke-width="1.8"/></svg></div>
  <h4>Email address :</h4>
  <p>info@companyname.com</p>
</div>

<div class="abs copy-bar">© Copyrights 2024 Company name | All Rights Reserved</div>

</body>
</html>
```